こんにちは、

森川建設の森川です!

弊社は、
八王子市で足場屋を営んでおります!

筋トレ大好きな若者向けの求人用のチラシを作ってもらいたいです。

アルバイト募集って感じで、

・ロングタイム
8:00〜17:00で1日16,000円

・ショートタイム
10:00〜16:00で1日13,000円

置き場などでの残業はありません。

筋肉、体幹を、鍛えて、
かつ、

ワンチャン技術も身につく!

※筋トレ好きや、格闘家や、アスリートに最適!

-----------------------------
弊社の売り(ここは、入れないほうが良ければ入れなくてもいいです!参考までに)

・会社の理念が、社員満足度を第一にして、会社と、関わる全ての人を潤わす。
・質の高い足場屋さん。技術力も優れている。
・週休2日制
・自分の用事に合わせて好きな日に休める。
・関わる全ての人が 経済的、精神的、時間的に潤うことを目指している。
・チームワークを大事にしている。
・全スタッフ14名
・イベント多数 (毎年海外旅行or国内旅行+レジャー)
・ホームページ morikawakensetsu.info

こんな感じなのですが、これを、イメージしてもらい、見る人に、インパクトと高感度を与えてくれて、口コミや、実際に応募がきたら嬉しいです。

㍿森川建設
A5
片面
シンプル 複雑
単色 カラフル
暗い 明るい
日常 高級
遊び心 厳粛
未来的 伝統的
女性的 男性的
一応会社のイメージカラーは、紺ですが、色は、オススメの色でお願いしたいです!
• 高解像度JPG (.jpg)
• イラストレーター形式 (.ai)
・バス広告のロゴで、バイアスを構築していますので、バス広告のデザインを利用して作っていただけると相乗効果を生むことができるので、お願いしたいです!

あ、このロゴなんか見たことあるのような感じです!
※ですが、上のロゴを入れるのが、あまり良くないと思えば、それは、気にしなくても良いです!1番は、若者を入れたいので、そのためを重視してもらいたいです!

・納品ですが、金額や、条件を少し編集できるようにしたいので、アウトライン化してるものと、されてないものを納品して頂きたいです!
A4でもA6でも使えるようにしたいです!
社内で話し合ったところ、もう少しインパクトの強い印象に残るものができるんじゃ無いかという期待を込めて延長させてもらいました。

・筋肉(鍛えられる)、
・短時間制のアルバイトがある(短時間制の職人系のアルバイトでは、珍しいです。)
・ロングタイムも、選べる。

これが1番伝えたい内容です。

次に、
職人さんは、いまとても減ってきてるので、希少性がかなり高くなっています。先に技術を学んでおくことで、後にブルーオーシャンになるのでは無いか?と予測しています。

これは、僕の伝えたい思い出もありますが、
チラシとして何を目的にしてるかは、
人を入れたいという事が目的なので、

ユーザー側の気持ちになってもらい、

・身体に自信がある人や
・身体にコンプレックスを持っていてムキムキになりたいと考えてる人
・頭を使うよりも身体を動かす事が自分に向いていると感じてる人に

響くような、チラシになることを願っています。

1発で目に引かれて、頭から離れないような、チラシにしてもらいたいです!

よろしくお願いします。

インパクトもあり、なんとなく清潔にも感じて、無駄な主張もなくシンプルで良い作品だと感じました。

多くの素晴らしい作品があり、選定するのにとても困りました。

本当にありがとうございます。

職人の価値向上を目指して、頑張ります!

本当にありがとうございました。

これからも宜しくお願い致します。

```html
<!DOCTYPE html>
<html lang="ja">
<head>
<meta charset="UTF-8">
<title>求人、足場職人｜森川建設</title>
<link rel="stylesheet" href="https://fonts.googleapis.com/css2?family=Noto+Sans+JP:wght@400;500;700;900&display=swap">
<style>
  :root{
    --ink:#111111;
    --dark:#1a1a1a;
    --lime:#b8d72c;
    --white:#ffffff;
    --grey:#6b6b6b;
    --photo-a:#5a5a5a;
    --photo-b:#0e0e0e;
  }
  *{box-sizing:border-box;margin:0;padding:0}
  html,body{width:848px;height:1200px;overflow:hidden;background:var(--white)}
  body{font-family:"Noto Sans JP",sans-serif;color:var(--ink)}
  .flyer{position:relative;width:848px;height:1200px;overflow:hidden;background:var(--white)}

  .hero{position:absolute;left:0;top:0;width:848px;height:560px;
    background:radial-gradient(ellipse at 38% 35%,var(--photo-a) 0%,#2b2b2b 45%,var(--photo-b) 80%);}

  .catch{position:absolute;right:44px;top:56px;text-align:right;color:var(--white);font-weight:900;line-height:1.15}
  .catch .line1{font-size:28px;letter-spacing:.04em}
  .catch .line2{font-size:28px;letter-spacing:.04em}
  .catch .line2 em{font-style:normal;color:var(--lime);font-size:58px;margin-left:6px}
  .catch-rule{position:absolute;right:44px;top:180px;width:290px;height:3px;background:var(--lime)}

  .perks{position:absolute;right:44px;top:204px;display:flex;flex-direction:column;gap:10px;align-items:flex-end}
  .perk{background:var(--lime);color:var(--ink);font-weight:900;font-size:22px;padding:3px 16px;min-width:168px;text-align:center;letter-spacing:.06em}

  .headline{position:absolute;left:48px;top:418px;color:var(--white);font-weight:900;font-size:96px;letter-spacing:-.02em;line-height:1}
  .headline-main{position:absolute;left:36px;top:528px;font-weight:900;font-size:132px;line-height:1;letter-spacing:-.03em;color:var(--ink)}

  .info{position:absolute;left:40px;top:676px;width:768px}
  .cols{display:flex;gap:30px}
  .col{flex:1}
  .sec-title{background:var(--ink);color:var(--white);font-weight:700;font-size:16px;padding:3px 12px;margin-bottom:6px;letter-spacing:.05em}
  .sec{margin-bottom:12px}
  .lead{font-weight:700;font-size:16px;line-height:1.4}
  .body{font-size:12.5px;line-height:1.55;color:#222}
  .note{font-size:11.5px;color:var(--grey)}

  .about{display:flex;gap:14px}
  .portrait{flex:0 0 78px;height:92px;background:linear-gradient(160deg,#c9c6c0,#7d7a75)}
  .rep{font-size:11px;text-align:right;color:var(--grey);margin-top:2px}

  .shift{border-top:2px solid var(--ink);padding:6px 0 4px}
  .shift-name{font-weight:900;font-size:16px}
  .shift-row{display:flex;justify-content:space-between;align-items:baseline}
  .shift-time{font-weight:700;font-size:18px}
  .shift-pay{font-weight:900;font-size:13px}
  .shift-pay b{font-size:32px;color:var(--ink)}

  .footer{position:absolute;left:0;bottom:0;width:848px;height:92px;background:var(--dark);color:var(--white);display:flex;align-items:center;padding:0 40px;gap:22px}
  .brand{display:flex;align-items:center;gap:8px;font-weight:900;font-size:22px}
  .brand-mark{width:22px;height:22px;background:var(--lime)}
  .contact{font-size:12px;line-height:1.5}
  .contact .tel{font-size:17px;font-weight:700}
  .hp{margin-left:auto;font-size:12px;line-height:1.5;text-align:right}
</style>
</head>
<body>
<div class="flyer">
  <div class="hero" role="img" aria-label="鍛えられた上半身の男性のモノクロ写真"></div>

  <div class="catch">
    <div class="line1">仕事で身に付ける</div>
    <div class="line2">ホンモノの<em>筋肉</em></div>
  </div>
  <div class="catch-rule"></div>

  <div class="perks">
    <div class="perk">未経験歓迎</div>
    <div class="perk">時短勤務可</div>
    <div class="perk">週休2日制</div>
  </div>

  <div class="headline">求人、</div>
  <div class="headline-main">足場職人</div>

  <div class="info">
    <div class="cols">
      <div class="col">
        <div class="sec">
          <div class="sec-title">募集職種</div>
          <p class="lead">鳶工事作業員【アルバイト】</p>
          <p class="body">今では需要が高い職種です。<br>職人の貴重な技術が身に付けられます！</p>
        </div>
        <div class="sec">
          <div class="sec-title">勤務場所</div>
          <p class="lead">八王子近辺、23区内</p>
          <p class="note">※置き場などでの残業はありません</p>
        </div>
      </div>
      <div class="col">
        <div class="sec">
          <div class="sec-title">勤務時間</div>
          <p class="body" style="margin-bottom:8px">ロングでガッツリ稼ぐ or ショートでプライベートと両立<br>働き方を2種類から選べます！</p>
          <div class="shift">
            <div class="shift-name">【ロングタイム】</div>
            <div class="shift-row"><span class="shift-time">8:00〜17:00</span><span class="shift-pay">日給 <b>16,000</b>円</span></div>
          </div>
          <div class="shift">
            <div class="shift-name">【ショートタイム】</div>
            <div class="shift-row"><span class="shift-time">10:00〜16:00</span><span class="shift-pay">日給 <b>13,000</b>円</span></div>
          </div>
        </div>
      </div>
    </div>
    <div class="sec">
      <div class="sec-title">森川建設について</div>
      <div class="about">
        <div class="portrait" role="img" aria-label="代表者の写真"></div>
        <div>
          <p class="body">弊社の理念は「社員満足度を第一にして、会社と関わる全ての人を潤わす」です。一緒に働いてくれる社員を大切に思うからこそ、働きやすい勤務環境づくりにも力を入れています。是非、私達の仲間として一緒に会社を盛り上げましょう！</p>
          <p class="rep">代表取締役 森川 大輔</p>
        </div>
      </div>
    </div>
  </div>

  <div class="footer">
    <div class="brand"><span class="brand-mark"></span>㍿森川建設</div>
    <div class="contact">
      〒192-0999 東京都八王子市緑町1-2-3<br>
      <span class="tel">TEL : 042-555-0187</span>　FAX : 042-555-0188
    </div>
    <div class="hp">会社の雰囲気をもっと知りたい方は<br>会社HPをご覧ください！<br>morikawakensetsu.info</div>
  </div>
</div>
</body>
</html>
```